Cover for Inspirational Daily Journal

This is the cover for a daily journal that will focus on inspirational content for black women. The cover should have a picture or silhouette of a black woman with a crown. The title is: "Grace in Bloom: A Year of Bright Mornings." The back won't have any words. Also the journal will be published on Pagewick.

```html
<!DOCTYPE html>
<html lang="en">
<head>
<meta charset="utf-8">
<title>Grace in Bloom: A Year of Bright Mornings — Cover</title>
<link rel="stylesheet" href="https://fonts.googleapis.com/css2?family=Playfair+Display:wght@500&family=Crimson+Text:ital@1&display=swap">
<style>
  :root {
    --page-bg: #f2f2f2;
    --gold-light: #f8eaa8;
    --gold-mid: #e2bf5c;
    --gold-deep: #b4872e;
    --gold-warm: #cfa346;
    --ink: #121010;
    --figure-fade: rgba(70, 48, 20, 0.55);
  }
  html, body {
    margin: 0;
    width: 1200px;
    height: 1200px;
    overflow: hidden;
    background: var(--page-bg);
  }
  .cover {
    position: absolute;
    left: 221px;
    top: 15px;
    width: 758px;
    height: 1168px;
    overflow: hidden;
    background:
      linear-gradient(160deg, transparent 0%, rgba(255,255,255,0) 48%, rgba(248,225,130,0.55) 62%, rgba(255,255,255,0) 74%),
      linear-gradient(170deg, var(--gold-light) 0%, var(--gold-mid) 22%, var(--gold-deep) 42%, var(--gold-warm) 60%, var(--gold-mid) 70%, var(--gold-deep) 90%, var(--gold-deep) 100%);
  }
  .cover-title {
    position: absolute;
    left: 0;
    top: 0;
    width: 758px;
    height: 360px;
  }
  .cover-title text {
    font-family: "Playfair Display", serif;
    font-weight: 500;
    fill: var(--ink);
  }
  .cover-figure {
    position: absolute;
    left: 250px;
    top: 318px;
    width: 280px;
    height: 725px;
    border-radius: 140px 140px 40px 40px;
    background: linear-gradient(180deg, var(--ink) 0%, var(--ink) 55%, var(--figure-fade) 85%, rgba(70,48,20,0) 100%);
  }
  .cover-subtitle {
    position: absolute;
    left: 0;
    width: 100%;
    top: 1028px;
    margin: 0;
    text-align: center;
    font-family: "Crimson Text", serif;
    font-style: italic;
    font-size: 46px;
    color: var(--ink);
  }
</style>
</head>
<body>
  <main class="cover">
    <svg class="cover-title" viewBox="0 0 758 360" aria-label="Grace in Bloom">
      <text x="57" y="147" font-size="148" textLength="650" lengthAdjust="spacingAndGlyphs">GRACE IN</text>
      <text x="54" y="310" font-size="200" textLength="650" lengthAdjust="spacingAndGlyphs">BLOOM</text>
    </svg>
    <div class="cover-figure" role="img" aria-label="Silhouette of a Black woman in profile wearing a crown, hand on hip, fading into the gold at the bottom"></div>
    <p class="cover-subtitle">A Year of Bright Mornings</p>
  </main>
</body>
</html>
```